Corvane Supplies Business Card

Professional business card that stand out to our potential customers. Front and back with clean modern design

Industry/Entity Type

Oil and gas

Contact Information for Business Card

Name, address, website , office phone and cell number

Requirements
Must have
• Editable files for each employee

```html
<!DOCTYPE html>
<html lang="en">
<head>
<meta charset="utf-8">
<title>Corvane Supplies Business Card</title>
<link href="https://fonts.googleapis.com/css2?family=Montserrat:wght@400;500;800&display=swap" rel="stylesheet">
<style>
  :root {
    --backdrop: #d6d6d6;
    --card: #2a2a2b;
    --red: #e8212a;
    --teal: #1fb1d4;
    --text: #f2f2f2;
    --pattern-teal: #2a7584;
    --pattern-mid: #5e5553;
    --pattern-red: #9e3128;
  }
  * { box-sizing: border-box; margin: 0; padding: 0; }
  html, body { width: 1200px; height: 880px; overflow: hidden; }
  body {
    background: var(--backdrop);
    font-family: "Montserrat", Arial, sans-serif;
    display: flex;
    flex-direction: column;
    align-items: center;
    justify-content: center;
    gap: 30px;
  }
  .card {
    width: 700px;
    height: 400px;
    background: var(--card);
    position: relative;
    box-shadow: 0 6px 18px rgba(0,0,0,0.25);
    overflow: hidden;
  }
  .card-back { padding: 14px; }
  .brand-pattern {
    width: 100%;
    height: 100%;
    background: linear-gradient(100deg, var(--pattern-teal) 0%, var(--pattern-mid) 48%, var(--pattern-red) 100%);
    opacity: 0.85;
  }
  .card-front {
    display: flex;
    align-items: center;
  }
  .brand {
    width: 355px;
    display: flex;
    align-items: center;
    justify-content: center;
    gap: 14px;
  }
  .brand-square {
    width: 34px;
    height: 34px;
    background: var(--teal);
  }
  .brand-name {
    font-weight: 800;
    font-size: 25px;
    letter-spacing: 1px;
    color: var(--red);
    text-transform: uppercase;
    line-height: 1.1;
  }
  .divider {
    width: 2px;
    height: 230px;
    background: var(--red);
  }
  .contact {
    padding-left: 26px;
    color: var(--text);
  }
  .person-name {
    font-weight: 800;
    font-size: 26px;
    color: var(--red);
    letter-spacing: 0.5px;
  }
  .person-title {
    font-size: 15px;
    font-weight: 500;
    margin-top: 2px;
  }
  .address {
    font-size: 14px;
    line-height: 1.4;
    margin-top: 16px;
  }
  .phones {
    font-size: 14px;
    line-height: 1.4;
    margin-top: 12px;
  }
  .links {
    list-style: none;
    margin-top: 10px;
  }
  .links li {
    display: flex;
    align-items: center;
    gap: 10px;
    font-size: 14px;
    line-height: 1.9;
  }
  .icon {
    width: 18px;
    height: 18px;
    background: var(--red);
    display: inline-flex;
    align-items: center;
    justify-content: center;
  }
  .icon svg { width: 12px; height: 12px; }
</style>
</head>
<body>
  <section class="card card-back">
    <div class="brand-pattern" role="img" aria-label="Repeating brand mark pattern shading from teal to red"></div>
  </section>

  <section class="card card-front">
    <div class="brand">
      <span class="brand-square"></span>
      <span class="brand-name">Corvane<br>Supplies</span>
    </div>
    <div class="divider"></div>
    <div class="contact">
      <h1 class="person-name">DALEN WHITCOMB</h1>
      <p class="person-title">President</p>
      <p class="address">418 Brenmoor Ave, Ste<br>100, Kelton, TX 75211</p>
      <p class="phones">555-014-2280<br>000-000-9999</p>
      <ul class="links">
        <li><span class="icon"><svg viewBox="0 0 12 12"><path d="M1 4 Q6 0 11 4 L10 5.5 L8 5 L8 4 Q6 3 4 4 L4 5 L2 5.5 Z M2.5 6 H9.5 V10.5 H2.5 Z" fill="#fff"/></svg></span>Office</li>
        <li><span class="icon"><svg viewBox="0 0 12 12"><rect x="3.5" y="1" width="5" height="10" rx="1" fill="none" stroke="#fff" stroke-width="1.2"/><circle cx="6" cy="9.3" r="0.6" fill="#fff"/></svg></span>Mobile</li>
        <li><span class="icon"><svg viewBox="0 0 12 12"><rect x="1" y="3" width="10" height="6.5" fill="none" stroke="#fff" stroke-width="1.1"/><path d="M1 3 L6 7 L11 3" fill="none" stroke="#fff" stroke-width="1.1"/></svg></span>info@example-youremail.com</li>
        <li><span class="icon"><svg viewBox="0 0 12 12"><circle cx="6" cy="6" r="4.6" fill="none" stroke="#fff" stroke-width="1.1"/><ellipse cx="6" cy="6" rx="2" ry="4.6" fill="none" stroke="#fff" stroke-width="0.9"/><path d="M1.4 6 H10.6" stroke="#fff" stroke-width="0.9"/></svg></span>www.example-yourwebsite.com</li>
      </ul>
    </div>
  </section>
</body>
</html>
```